Vireno Subscription Infographic

I need an infographic to promote my new subscription service.
The infographic should be clear and consise, showcasing the benefits and the value of my offering.
I have provided a PDF that describes the service, and the offering in detail. I would like the designer to read the pdf document, understand the offering and design a one page infographic that will condense the information in a nice, visual way, to be shared within Workvine for advertisment purposes.

```html
<!DOCTYPE html>
<html lang="en">
<head>
<meta charset="utf-8">
<title>Vireno Subscription Packages</title>
<link rel="stylesheet" href="https://fonts.googleapis.com/css2?family=League+Gothic&family=Oswald:wght@600&family=Poppins:ital,wght@0,400;0,500;0,600;0,700;1,400;1,500&family=Space+Mono:wght@700&display=swap">
<style>
:root{
  --navy:#1f2a5e;
  --navy-dark:#1a2350;
  --light-bg:#f1f1f4;
  --orange:#f5921e;
  --blue:#1b75c4;
  --sky:#5db4e5;
  --green:#6cbf5c;
  --salmon:#f9d0c0;
  --white:#ffffff;
  --ink:#2a2f45;
}
*{margin:0;padding:0;box-sizing:border-box}
html,body{width:1200px;height:4322px;overflow:hidden}
body{position:relative;background:var(--light-bg);font-family:"Poppins",sans-serif;color:var(--ink)}
.abs{position:absolute}

.band-navy{position:absolute;left:0;width:1200px;background:var(--navy)}
.blob{position:absolute;border-radius:50%}

.quote-mark{left:80px;top:40px;font-family:"Poppins",sans-serif;font-weight:700;font-size:260px;line-height:1;color:var(--orange)}
.tagline{left:260px;top:118px;color:var(--white);font-weight:500;font-size:35px;line-height:46px}
.brand{left:762px;top:104px;display:flex;align-items:center;gap:22px}
.brand-dot{width:104px;height:104px;border-radius:50%;border:7px solid var(--white)}
.brand-name{color:var(--white);font-weight:600;font-size:72px;line-height:1}
.page-title{left:82px;top:284px;width:1040px;font-family:"League Gothic",sans-serif;font-size:122px;line-height:1;color:var(--white);letter-spacing:1px;text-align:center}

.pkg-table{left:81px;top:423px;display:flex;gap:2px}
.pkg-col{width:171px;background:var(--dk);border-radius:14px;overflow:hidden;padding-bottom:22px}
.pkg-col .cell{height:65px;display:flex;align-items:center;justify-content:center;text-align:center;font-size:15px;line-height:1.15;padding:0 6px}
.pkg-col .cell.head{height:74px;background:var(--hd);color:var(--hd-text);font-weight:600;font-size:20px}
.pkg-col .cell.lt{background:var(--lt);color:var(--ink)}
.pkg-col .cell.dk{color:var(--dk-text)}
.pkg-col .cell.tools{font-weight:600;font-size:20px;line-height:1.1}
.pkg-col .cell.small{font-size:14px}
.col-sub{--hd:#9dc3e6;--hd-text:var(--navy);--lt:#e8f2fb;--dk:#9fc5e8;--dk-text:var(--navy)}
.col-starter{--hd:#d5d9cc;--hd-text:var(--ink);--lt:#eef0e8;--dk:#d6d9ce;--dk-text:var(--ink)}
.col-entry{--hd:#a868b0;--hd-text:#fff;--lt:#f0e2f2;--dk:#a566ad;--dk-text:#fff}
.col-member{--hd:#8fa27c;--hd-text:#fff;--lt:#e9eee2;--dk:#8ea37c;--dk-text:#fff}
.col-premium{--hd:#f5921e;--hd-text:#fff;--lt:#fde6cd;--dk:#f5921e;--dk-text:#fff}
.col-exclusive{--hd:#1b75c4;--hd-text:#fff;--lt:#e1edf8;--dk:#1b75c4;--dk-text:#fff}
.col-sub .cell.tools,.col-starter .cell.tools{color:var(--navy)}

.apart-heading{left:92px;top:1616px;font-family:"Oswald",sans-serif;font-weight:600;font-size:76px;line-height:93px;color:var(--white);letter-spacing:1px}
.apart-heading .hl{background:var(--orange);color:var(--navy);padding:0 8px}
.team-art{left:700px;top:1556px;width:416px;height:440px;border-radius:20px;background:linear-gradient(160deg,#e9eef9 0%,#9fb4e4 55%,#3b5cb0 100%)}
.deco-square{left:890px;top:1552px;width:18px;height:18px;background:var(--blue)}

.tab{top:2039px;height:50px;border-radius:12px 12px 0 0;color:var(--white);font-weight:600;font-size:26px;display:flex;align-items:center;justify-content:center}
.offer-col{left:91px;top:2089px;width:362px;display:flex;flex-direction:column;gap:6px}
.status-col{left:747px;top:2089px;width:362px;display:flex;flex-direction:column;gap:6px}
.offer-row{display:flex;align-items:center;padding:0 16px;font-size:15px;line-height:1.25;color:var(--ink)}
.status-row{display:flex;align-items:center;padding-left:110px;gap:14px;color:var(--white);font-size:21px}
.tick{width:32px;height:32px;border-radius:50%;background:var(--white);display:flex;align-items:center;justify-content:center}
.desc-col{left:453px;top:2089px;width:294px;height:521px;background:var(--salmon);display:flex;align-items:center;justify-content:center;text-align:center;font-size:35px;line-height:45px;color:var(--ink);padding:0 20px}

.meeting-art{left:117px;top:2676px;width:455px;height:354px;border-radius:18px;background:linear-gradient(180deg,#e4e7ef 0%,#f6c78c 45%,#cdd1dd 100%)}
.art-label{font-size:15px;font-weight:600;color:var(--ink);line-height:1.2}
.sprint-bar{left:96px;top:3037px;width:483px;height:70px;background:var(--navy);color:var(--white);font-weight:600;font-size:35px;display:flex;align-items:center;justify-content:center}
.approach-head{left:629px;top:2718px;width:482px;height:88px;background:var(--orange);font-family:"League Gothic",sans-serif;font-size:72px;color:var(--navy);display:flex;align-items:center;justify-content:center;letter-spacing:1px}
.approach-item{left:629px;width:482px;height:90px;background:var(--white);display:flex;align-items:center;justify-content:space-between;padding:0 28px 0 34px;font-family:"League Gothic",sans-serif;font-size:72px;color:var(--navy);box-shadow:0 4px 8px rgba(0,0,0,.12)}
.approach-item svg{width:78px;height:78px}

.target-art{left:110px;top:3240px;width:540px;height:540px;border-radius:50%;background:radial-gradient(circle,#f7a64a 0%,#f5921e 40%,#e57f10 100%)}
.steps{left:696px;top:3200px;width:420px}
.step{display:flex;align-items:center;gap:18px;height:110px;border-bottom:3px dashed #7e86b5}
.step:last-child{border-bottom:none}
.step-num{flex:none;font-size:74px;font-weight:500;color:var(--sky);width:44px;text-align:center;line-height:1}
.step-text{font-style:italic;font-size:22px;line-height:27px;color:var(--ink);white-space:nowrap}

.terms-title{left:70px;top:3966px;font-family:"Space Mono",monospace;font-size:50px;color:var(--orange);line-height:1}
.terms{left:68px;top:4044px;width:540px}
.term{display:flex;gap:18px;align-items:flex-start;margin-bottom:22px}
.term-num{flex:none;width:34px;height:34px;border-radius:50%;background:var(--white);color:var(--navy);font-weight:700;font-size:19px;display:flex;align-items:center;justify-content:center}
.term-text{font-style:italic;font-size:15px;line-height:20px;color:var(--white)}
.card-back{left:688px;top:3996px;width:450px;height:242px;border-radius:16px;background:#c9cde0}
.card{left:666px;top:3973px;width:450px;height:242px;border-radius:16px;background:#f3f3f6;padding:34px 24px}
.card-name{font-weight:700;font-size:25px;line-height:32px;color:var(--navy)}
.card-badge{left:290px;top:32px;width:131px;height:44px;border-radius:10px;background:var(--navy);display:flex;align-items:center;justify-content:center;gap:8px;color:var(--white);font-weight:600;font-size:22px}
.card-badge span.dot{width:20px;height:20px;border-radius:50%;border:3px solid var(--white)}
.card-contact{position:absolute;left:24px;top:158px;font-weight:600;font-size:20px;line-height:34px;color:var(--navy)}
</style>
</head>
<body>

<div class="band-navy" style="top:0;height:487px"></div>
<div class="blob" style="left:-150px;top:1250px;width:220px;height:240px;background:#5cb85c"></div>
<div class="band-navy" style="top:1376px;height:1384px"></div>
<div class="blob" style="left:1140px;top:2390px;width:150px;height:190px;background:var(--blue)"></div>
<div class="band-navy" style="top:3918px;height:404px"></div>
<div class="blob" style="left:860px;top:4080px;width:440px;height:440px;background:var(--orange)"></div>

<div class="abs quote-mark">&ldquo;</div>
<div class="abs tagline">Your Partner<br>in Electrification</div>
<div class="abs brand"><span class="brand-dot"></span><span class="brand-name">Vireno</span></div>
<h1 class="abs page-title">SUBSCRIPTION PACKAGES LIST</h1>

<div class="abs pkg-table">
  <div class="pkg-col col-sub">
    <div class="cell head">Subscription</div>
    <div class="cell lt">Full Time<br>Equivalent</div>
    <div class="cell dk">Price<br>(Monthly)</div>
    <div class="cell lt">Engineering<br>Hours Pool</div>
    <div class="cell dk">Equivalent<br>Hourly Price</div>
    <div class="cell lt">OnSite<br>Support</div>
    <div class="cell dk tools">Tools<br>Access</div>
    <div class="cell lt"></div><div class="cell dk"></div><div class="cell lt"></div><div class="cell dk"></div><div class="cell lt"></div><div class="cell dk"></div><div class="cell lt"></div><div class="cell dk"></div><div class="cell lt"></div>
  </div>
  <div class="pkg-col col-starter">
    <div class="cell head">Starter</div>
    <div class="cell lt">1 FTE</div>
    <div class="cell dk">$9,280</div>
    <div class="cell lt">160</div>
    <div class="cell dk">$58</div>
    <div class="cell lt">Online Support<br>Only</div>
    <div class="cell dk tools">Mainstream<br>Tools</div>
    <div class="cell lt small">Emails accounts<br>DeskOffice<br>Plangantt</div>
    <div class="cell dk"></div><div class="cell lt"></div><div class="cell dk"></div><div class="cell lt"></div><div class="cell dk"></div><div class="cell lt"></div><div class="cell dk"></div><div class="cell lt"></div>
  </div>
  <div class="pkg-col col-entry">
    <div class="cell head">Entry</div>
    <div class="cell lt">2 FTE</div>
    <div class="cell dk">$17,120</div>
    <div class="cell lt">320</div>
    <div class="cell dk">$53.5</div>
    <div class="cell lt small">1 Engineer<br>Semi-per name<br>evently on site</div>
    <div class="cell dk tools">Mainstream<br>Tools</div>
    <div class="cell lt small">Emails accounts<br>DeskOffice<br>Plangantt</div>
    <div class="cell dk">Engineering<br>Tools</div>
    <div class="cell lt small">Relysa Vireno in<br>house Calculators</div>
    <div class="cell dk"></div><div class="cell lt"></div><div class="cell dk"></div><div class="cell lt"></div><div class="cell dk"></div><div class="cell lt"></div>
  </div>
  <div class="pkg-col col-member">
    <div class="cell head">Member</div>
    <div class="cell lt">3 FTE</div>
    <div class="cell dk">$24,900</div>
    <div class="cell lt">480</div>
    <div class="cell dk">$51.9</div>
    <div class="cell lt small">1 Engineer<br>Semi-per name<br>evently on site</div>
    <div class="cell dk tools">Mainstream<br>Tools</div>
    <div class="cell lt small">Emails accounts<br>DeskOffice<br>Plangantt</div>
    <div class="cell dk">Engineering<br>Tools</div>
    <div class="cell lt small">Relysa Vireno in<br>house Calculators</div>
    <div class="cell dk">Specialist<br>Tools</div>
    <div class="cell lt">Numlab<br>Tramvex</div>
    <div class="cell dk"></div><div class="cell lt"></div><div class="cell dk"></div><div class="cell lt"></div>
  </div>
  <div class="pkg-col col-premium">
    <div class="cell head">Premium</div>
    <div class="cell lt">4 FTE</div>
    <div class="cell dk">$32,000</div>
    <div class="cell lt">640</div>
    <div class="cell dk">$50</div>
    <div class="cell lt small">1 Engineer<br>Semi-per name<br>evently on site</div>
    <div class="cell dk tools">Mainstream<br>Tools</div>
    <div class="cell lt small">Emails accounts<br>DeskOffice<br>Plangantt</div>
    <div class="cell dk">Engineering<br>Tools</div>
    <div class="cell lt small">Relysa Vireno in<br>house Calculators</div>
    <div class="cell dk">Specialist<br>Tools</div>
    <div class="cell lt">Numlab<br>Tramvex</div>
    <div class="cell dk">High End<br>Software</div>
    <div class="cell lt">MotorDes<br>Anvyx(Mech)</div>
    <div class="cell dk"></div><div class="cell lt"></div>
  </div>
  <div class="pkg-col col-exclusive">
    <div class="cell head">Exclusive</div>
    <div class="cell lt">5 FTE</div>
    <div class="cell dk">$39,600</div>
    <div class="cell lt">800</div>
    <div class="cell dk">$49.5</div>
    <div class="cell lt small">1 Engineer<br>Semi-per name<br>evently on site</div>
    <div class="cell dk tools">Mainstream<br>Tools</div>
    <div class="cell lt small">Emails accounts<br>DeskOffice<br>Plangantt</div>
    <div class="cell dk">Engineering<br>Tools</div>
    <div class="cell lt small">Relysa Vireno in<br>house Calculators</div>
    <div class="cell dk">Specialist<br>Tools</div>
    <div class="cell lt">Numlab<br>Tramvex</div>
    <div class="cell dk">High End<br>Software</div>
    <div class="cell lt">MotorDes<br>Anvyx(Mech)</div>
    <div class="cell dk">Specialist<br>Software</div>
    <div class="cell lt small">ROVEX MultiBody<br>Dynamics</div>
  </div>
</div>

<h2 class="abs apart-heading">WHAT <span class="hl">SETS</span><br><span class="hl">US APART</span> FROM<br>COMPETITION</h2>
<svg class="abs" style="left:330px;top:1840px" width="310" height="190" viewBox="0 0 310 190" aria-hidden="true">
  <path d="M295 10 C270 110 160 150 30 165" fill="none" stroke="#f5921e" stroke-width="7" stroke-linecap="round"/>
  <path d="M55 140 L22 166 L58 185" fill="none" stroke="#f5921e" stroke-width="7" stroke-linecap="round" stroke-linejoin="round"/>
</svg>
<div class="abs deco-square"></div>
<div class="abs team-art" role="img" aria-label="Illustration of two engineers collaborating with notes and a tablet"></div>

<div class="abs tab" style="left:163px;width:198px;background:var(--green)">Offering</div>
<div class="abs tab" style="left:500px;width:200px;background:var(--orange)">Description</div>
<div class="abs tab" style="left:831px;width:198px;background:var(--blue)">Status</div>

<div class="abs offer-col">
  <div class="offer-row" style="height:104px;background:#a5d39a">Flexible systems engineering support including but not limited to : MBSE, FMEA, requirements management and DVP creation</div>
  <div class="offer-row" style="height:71px;background:#b6dcaa">Power Electronics and Inverter Development Engineer Support</div>
  <div class="offer-row" style="height:77px;background:#c2e1b7">Safety Engineer and DMFEA/Fault Tree Expert Support</div>
  <div class="offer-row" style="height:87px;background:#a9d49e">Project Management and Engineering Management</div>
  <div class="offer-row" style="height:80px;background:#a0d095">Onsite Support(Harrow)</div>
  <div class="offer-row" style="height:72px;background:#6cbf5c">eMachine Design Engineer</div>
</div>
<div class="abs desc-col">See Subscription Levels for FTE Equivalent</div>
<div class="abs status-col">
  <div class="status-row" style="height:104px;background:#5b8fd6"><span class="tick"><svg width="18" height="18" viewBox="0 0 18 18"><path d="M3 9.5 L7.5 14 L15 5" fill="none" stroke="#5b8fd6" stroke-width="3" stroke-linecap="round" stroke-linejoin="round"/></svg></span>Included</div>
  <div class="status-row" style="height:71px;background:#6f9ddc"><span class="tick"><svg width="18" height="18" viewBox="0 0 18 18"><path d="M3 9.5 L7.5 14 L15 5" fill="none" stroke="#6f9ddc" stroke-width="3" stroke-linecap="round" stroke-linejoin="round"/></svg></span>Included</div>
  <div class="status-row" style="height:77px;background:#86ade2"><span class="tick"><svg width="18" height="18" viewBox="0 0 18 18"><path d="M3 9.5 L7.5 14 L15 5" fill="none" stroke="#86ade2" stroke-width="3" stroke-linecap="round" stroke-linejoin="round"/></svg></span>Included</div>
  <div class="status-row" style="height:87px;background:#5b8fd6"><span class="tick"><svg width="18" height="18" viewBox="0 0 18 18"><path d="M3 9.5 L7.5 14 L15 5" fill="none" stroke="#5b8fd6" stroke-width="3" stroke-linecap="round" stroke-linejoin="round"/></svg></span>Included</div>
  <div class="status-row" style="height:80px;background:#4a86d2"><span class="tick"><svg width="18" height="18" viewBox="0 0 18 18"><path d="M3 9.5 L7.5 14 L15 5" fill="none" stroke="#4a86d2" stroke-width="3" stroke-linecap="round" stroke-linejoin="round"/></svg></span>Included</div>
  <div class="status-row" style="height:72px;background:#1b75c4"><span class="tick"><svg width="18" height="18" viewBox="0 0 18 18"><path d="M3 9.5 L7.5 14 L15 5" fill="none" stroke="#1b75c4" stroke-width="3" stroke-linecap="round" stroke-linejoin="round"/></svg></span>Included</div>
</div>

<div class="abs meeting-art" role="img" aria-label="Illustration of a project manager and a lead customer engineer in a Monday meeting with speech bubbles"></div>
<div class="abs art-label" style="left:72px;top:2900px">Project<br>Manager</div>
<div class="abs art-label" style="left:524px;top:2834px">Lead<br>Customer<br>Engineer</div>
<div class="abs sprint-bar">Sprint Design Meeting</div>

<div class="abs approach-head">WORK APPROACH</div>
<div class="abs approach-item" style="top:2819px">FLEXIBILITY
  <svg viewBox="0 0 80 80" aria-hidden="true"><rect x="8" y="14" width="60" height="56" rx="6" fill="#2a4d9c"/><rect x="8" y="14" width="60" height="14" rx="6" fill="#1f2a5e"/><rect x="20" y="6" width="6" height="16" rx="3" fill="#1f2a5e"/><rect x="50" y="6" width="6" height="16" rx="3" fill="#1f2a5e"/><path d="M26 50 a14 14 0 0 1 26 -6 M54 52 a14 14 0 0 1 -26 6" fill="none" stroke="#fff" stroke-width="4" stroke-linecap="round"/></svg>
</div>
<div class="abs approach-item" style="top:2921px">TRANSPARENCY
  <svg viewBox="0 0 80 80" aria-hidden="true"><circle cx="40" cy="40" r="36" fill="#1f2a5e"/><circle cx="36" cy="36" r="16" fill="#f7b6c8" stroke="#fff" stroke-width="4"/><path d="M48 48 L62 62" stroke="#fff" stroke-width="6" stroke-linecap="round"/></svg>
</div>
<div class="abs approach-item" style="top:3020px">COLLABORATION
  <svg viewBox="0 0 80 80" aria-hidden="true"><path d="M6 30 L20 22 L40 34 L60 22 L74 30 L74 46 L54 60 L40 54 L26 60 L6 46 Z" fill="none" stroke="#1f2a5e" stroke-width="5" stroke-linejoin="round"/><path d="M30 40 L44 52" stroke="#1f2a5e" stroke-width="5" stroke-linecap="round"/></svg>
</div>

<div class="abs target-art" role="img" aria-label="Illustration of a target with an arrow in the centre, labelled Primary Goal"></div>
<div class="abs steps">
  <div class="step"><span class="step-num">1</span><span class="step-text">Clearly Define And Agree Upon<br>The Week's Deliverables</span></div>
  <div class="step"><span class="step-num">2</span><span class="step-text">Ensuring Both Teams Are<br>Fully Synchronized</span></div>
  <div class="step"><span class="step-num">3</span><span class="step-text">Bi-weekly Standup Meetings<br>To Ensure Transparency</span></div>
  <div class="step"><span class="step-num">4</span><span class="step-text">Discuss<br>Challenges</span></div>
  <div class="step"><span class="step-num">5</span><span class="step-text">Update On Progress<br>With Team Members</span></div>
  <div class="step"><span class="step-num">6</span><span class="step-text">Swiftly Address<br>Potential Bottlenecks</span></div>
</div>

<h2 class="abs terms-title">Additional Terms</h2>
<div class="abs terms">
  <div class="term"><span class="term-num">1</span><p class="term-text">Subscription Level can be adjusted on a 3 month notice<br>(higher/lower number of FTE hours)</p></div>
  <div class="term"><span class="term-num">2</span><p class="term-text">If project needs increase, upgrades on the service can be delivered potentially earlier, pending Vireno engineering team availability.</p></div>
  <div class="term"><span class="term-num">3</span><p class="term-text">If project needs are reduced, with a 3 month notice we can reallocate the resources to other customers, effectively being able to reduce the subscription service levels</p></div>
</div>
<div class="abs card-back"></div>
<div class="abs card">
  <p class="card-name">Elias Marendos<br>Director</p>
  <div class="abs card-badge"><span class="dot"></span>Vireno</div>
  <p class="card-contact">+44 (0) 7700 900123<br>ELIAS@VIRENO-TECH.COM</p>
</div>

</body>
</html>
```